Online Marketplace Startup for Community Facilities (Tovaroom)

A innovative, modern website design is required for a new startup called Tovaroom. Tovaroom will be an online marketplace for searching for and booking community facilities, such as schools facilities (sports grounds, halls, classrooms etc.), churches, hospitals and other community facilities.

The attached brief has been created to provide guidance on the structure and content required.

The web design shall feature a modern, innovative but user friendly interface similar style to other web start up pages:
www.hallquiver.co.uk
www.vendlark.com.au
www.artfennel.com.au

The web design shall be ‘wordpress’ compliant and allow for future functionality to be added and coded (e.g. animations, flash, blogs etc) and content to be editable.

The following brief has been created to provide guidance on the structure and content required.

An existing logo developed for Tovaroom shall be utilised and incorporated in the top left hand cover of the cover landing page (refer to attached logo designs).

Refer to attached 'Website brief' for more details on requirements.
Updates

Project Deadline Extended
Reason: I wish to grant an extension to the deadline to provide designers with more time to submit their designs.

Target Market(s)

TovaRoom will focus on building a customer network of both community facility owners (schools, hospitals, churches) and hirers (non-government organisations, community groups, event management companies, commercial businesses). Members of the general public will also be encouraged to book facilities for private functions.

Industry/Entity Type

Community

Coding

Coded - Design and coding required

Number of Pages Required

5+ page

Font styles to use
Sans Serif

Colors
3176b5
ffffff
85cae6
33a6d7

Requirements
Must have
• The web design shall feature a modern, innovative but user friendly interface similar style to other web start up pages:
• www.hallquiver.co.uk
• www.vendlark.com.au
• www.artfennel.com.au
• The web design shall be ‘wordpress’ compliant and allow for future functionality to be added and coded (e.g. animations, flash, blogs etc) and content to be editable.
• Refer to Project brief for other requirements
Nice to have
• Refer to Project brief
Should not have
• Refer to Project brief

```html
<!DOCTYPE html>
<html lang="en">
<head>
<meta charset="utf-8">
<title>TovaRoom – Community Facility Bookings</title>
<link href="https://fonts.googleapis.com/css2?family=Raleway:wght@400;500;600&family=Open+Sans:wght@400;600&display=swap" rel="stylesheet">
<style>
:root{
  --brand:#3176b5;
  --navy:#1d3f73;
  --sky:#33a6d7;
  --sky-light:#85cae6;
  --white:#ffffff;
  --ink:#333333;
  --muted:#666666;
  --grey-bg:#ebe9ea;
  --footer:#3d3d3f;
  --footer-text:#d6d6d6;
}
*{box-sizing:border-box;margin:0;padding:0}
html,body{width:679px;height:1200px;overflow:hidden;background:var(--white)}
body{position:relative;font-family:"Open Sans",Arial,sans-serif;color:var(--ink)}
.abs{position:absolute}
.heading{font-family:"Raleway",Arial,sans-serif}

/* top bar */
.topbar{left:0;top:0;width:679px;height:25px;background:var(--brand)}
.social{display:flex;gap:4px}
.social span{width:14px;height:14px;border-radius:50%;background:var(--white);display:block}
.topbar .social{position:absolute;left:522px;top:6px}

/* nav */
.nav{left:0;top:25px;width:679px;height:47px;background:var(--white);border-bottom:1px solid #e4e4e4}
.brand{display:flex;align-items:center;gap:6px;font-family:"Raleway",Arial,sans-serif;font-weight:500}
.brand-mark{width:14px;height:14px;background:var(--navy)}
.nav .brand{position:absolute;left:90px;top:12px;font-size:19px;color:var(--navy)}
.menu{position:absolute;left:246px;top:19px;display:flex;gap:12px;font-size:7.4px;list-style:none;color:#333}
.menu li.active{color:var(--sky)}

/* hero */
.hero{left:0;top:72px;width:679px;height:286px;background:linear-gradient(120deg,#2aa4dd 0%,#33a6d7 50%,#2b9bd3 100%);color:var(--white)}
.hero h1{position:absolute;left:90px;top:78px;font-size:27px;font-weight:500;font-family:"Raleway",Arial,sans-serif}
.hero p{position:absolute;left:90px;top:118px;width:230px;font-size:10.3px;line-height:16px;font-family:"Raleway",Arial,sans-serif}
.btn-outline-light{position:absolute;left:93px;top:174px;width:86px;height:28px;border:2px solid var(--white);font-size:9.5px;font-weight:600;letter-spacing:.3px;display:flex;align-items:center;justify-content:center;font-family:"Raleway",Arial,sans-serif}
.hero-art{position:absolute;left:336px;top:8px;width:343px;height:278px;background:radial-gradient(ellipse at 55% 45%,#e9ecef 0%,#b9dff2 35%,rgba(51,166,215,0) 70%)}
.dots{position:absolute;left:323px;top:261px;display:flex;gap:3px}
.dots span{width:8px;height:8px;border-radius:50%;background:var(--white)}
.dots span.off{background:transparent;border:1.5px solid var(--white)}

/* about */
.about{left:0;top:358px;width:679px;height:250px;background:var(--white)}
.about h2{position:absolute;left:90px;top:46px;font-size:17.5px;font-weight:500;color:var(--navy)}
.about p{position:absolute;left:92px;width:232px;font-size:7.4px;line-height:13.5px;color:var(--muted)}
.about .p1{top:77px}
.about .p2{top:110px}
.btn-outline{position:absolute;left:93px;top:167px;width:81px;height:20px;border:1px solid var(--brand);color:var(--brand);font-size:8.3px;display:flex;align-items:center;justify-content:center}
.about-art{position:absolute;left:336px;top:10px;width:272px;height:204px;background:radial-gradient(ellipse at center,#dcebf7 0%,#f1f7fc 50%,#ffffff 75%)}

/* services */
.services{left:0;top:608px;width:679px;height:222px;background:var(--grey-bg)}
.services .badge{position:absolute;left:328px;top:-12px;width:28px;height:28px;background:var(--white);transform:rotate(45deg)}
.services h2{position:absolute;left:0;width:679px;top:28px;text-align:center;font-size:17px;font-weight:500;color:var(--navy)}
.service{position:absolute;top:70px;width:120px;text-align:center}
.service .diamond{width:60px;height:60px;margin:8px auto 0;background:var(--brand);transform:rotate(45deg);display:flex;align-items:center;justify-content:center}
.service .diamond svg{transform:rotate(-45deg)}
.service p{margin-top:15px;font-family:"Raleway",Arial,sans-serif;font-size:9.3px;line-height:14px;font-weight:500;color:var(--ink)}
.arrow{position:absolute;top:96px}

/* enquiry */
.enquiry{left:0;top:830px;width:679px;height:204px;background:linear-gradient(110deg,#2f6fc4 0%,#3a86d6 50%,#2b6fc6 100%);color:var(--white)}
.enquiry h2{position:absolute;left:0;width:679px;top:18px;text-align:center;font-size:15px;font-weight:500}
.enquiry .sub{position:absolute;left:0;width:679px;top:41px;text-align:center;font-size:9.3px;font-family:"Raleway",Arial,sans-serif}
.field{position:absolute;left:162px;width:177px;height:20px;background:var(--white);color:#444;font-size:6.5px;padding:7px 0 0 5px}
.select-caret{position:absolute;right:0;top:0;width:16px;height:20px;background:#e3e3e3;display:flex;align-items:center;justify-content:center}
.comments{position:absolute;left:345px;top:68px;width:177px;height:88px;background:var(--white);color:#444;font-size:6.5px;padding:6px 5px}
.submit{position:absolute;left:162px;top:162px;width:66px;height:21px;background:var(--sky);font-size:7.5px;font-weight:600;letter-spacing:1px;display:flex;align-items:center;justify-content:center}

/* footer */
.footer{left:0;top:1034px;width:679px;height:166px;background:var(--footer);color:var(--footer-text)}
.footer .brand{position:absolute;left:92px;top:23px;font-size:16px;color:var(--white)}
.footer .brand-mark{background:var(--white);width:11px;height:11px}
.footer .about-text{position:absolute;left:92px;top:61px;width:175px;font-size:6px;line-height:12.5px}
.footer h3{position:absolute;top:25px;font-size:8.3px;font-weight:400;color:var(--white);font-family:"Open Sans",Arial,sans-serif}
.footer-links{position:absolute;left:259px;top:45px;list-style:none;font-size:6.2px;line-height:10.6px}
.contact{position:absolute;left:356px;top:44px;font-size:6.2px;line-height:12.8px;list-style:none}
.contact li{display:flex;gap:6px}
.contact svg{flex:none;margin-top:3px}
.footer .social{position:absolute;left:522px;top:46px}
.footer .social span{width:13px;height:13px;background:var(--brand)}
.footer .social span:nth-child(2){background:var(--sky)}
.footer .social span:nth-child(3){background:#d9534f}
.footer .social span:nth-child(4){background:#2b6fb2}
.divider{position:absolute;left:92px;top:126px;width:496px;height:1px;background:#555}
.copyright{position:absolute;left:0;width:679px;top:140px;text-align:center;font-size:5.8px}
</style>
</head>
<body>

<header class="abs topbar">
  <div class="social" aria-label="Social links"><span></span><span></span><span></span><span></span></div>
</header>

<nav class="abs nav">
  <div class="brand"><span class="brand-mark"></span>TovaRoom</div>
  <ul class="menu">
    <li class="active">Home</li><li>About Us</li><li>How it Works</li><li>Services</li><li>Packages</li><li>Why Us?</li><li>News</li><li>FAQ</li><li>Contact Us</li>
  </ul>
</nav>

<section class="abs hero">
  <h1>TovaRoom</h1>
  <p>Lorem ipsum dolor sit amet, consectetur ipiscing elit, sed do eiusmod tempor incidi dunt ut labore et dolore magndolo.</p>
  <div class="btn-outline-light">READ MORE</div>
  <div class="hero-art" role="img" aria-label="Illustration of a desk with laptop, coffee cup, glasses, phone and a hand on a mouse"></div>
  <div class="dots"><span></span><span></span><span class="off"></span><span></span></div>
</section>

<section class="abs about">
  <h2 class="heading">About TovaRoom</h2>
  <p class="p1">Pellentesque faucibus Ut accumsan ultricies elit Maecenas at justo id velit placerat molestie Donec dictum lectus non odio</p>
  <p class="p2">nec euismod sit amet egestas placerat est Pellentesque habitant morbi tristique senectus et netus et malesuada fames ac turpis egestas Cras id elit Integer quis urna Ut ante</p>
  <div class="btn-outline">Read More</div>
  <div class="about-art" role="img" aria-label="Line-art network of business icons connected by thin circuit lines"></div>
</section>

<section class="abs services">
  <div class="badge"></div>
  <h2 class="heading">Our Services</h2>

  <svg class="arrow" style="left:68px" width="12" height="20" viewBox="0 0 12 20"><path d="M10 2 2 10l8 8" fill="none" stroke="#999" stroke-width="2"/></svg>
  <svg class="arrow" style="left:600px" width="12" height="20" viewBox="0 0 12 20"><path d="M2 2l8 8-8 8" fill="none" stroke="#999" stroke-width="2"/></svg>

  <div class="service" style="left:85px">
    <div class="diamond"><svg width="30" height="26" viewBox="0 0 30 26" fill="none" stroke="#fff" stroke-width="1.3"><path d="M3 10h5l12-7v20L8 16H3z"/><path d="M8 16l2 7h3l-2-7"/><path d="M24 9l4-2M24 13h5M24 17l4 2"/></svg></div>
    <p>Marketing and<br>Promotion of your facility</p>
  </div>
  <div class="service" style="left:217px;top:66px">
    <div class="diamond"><svg width="30" height="26" viewBox="0 0 30 26" fill="none" stroke="#fff" stroke-width="1.3"><rect x="2" y="4" width="22" height="15"/><path d="M13 19v4M8 23h10"/><rect x="16" y="1" width="11" height="7" fill="#3176b5"/><circle cx="8" cy="12" r="1"/><circle cx="12" cy="12" r="1"/><circle cx="16" cy="12" r="1"/></svg></div>
    <p>Administer Bookings<br>and Enquiries</p>
  </div>
  <div class="service" style="left:349px;top:66px">
    <div class="diamond"><svg width="24" height="28" viewBox="0 0 24 28" fill="none" stroke="#fff" stroke-width="1.3"><path d="M4 2h14v22l-2-2-2 2-2-2-2 2-2-2-2 2-2-2z"/><path d="M7 8h8M7 12h8M7 16h5"/></svg></div>
    <p>Invoicing and<br>Payment collection</p>
  </div>
  <div class="service" style="left:481px;top:66px">
    <div class="diamond"><svg width="30" height="26" viewBox="0 0 30 26" fill="none" stroke="#fff" stroke-width="1.3"><rect x="2" y="2" width="26" height="16"/><path d="M15 18v5M9 23h12"/><path d="M6 14l6-5 5 3 7-7"/></svg></div>
    <p>Bookings Reports<br>and Customer Service</p>
  </div>
</section>

<section class="abs enquiry">
  <h2 class="heading">Enquiry Form</h2>
  <p class="sub">Lorem ipsum dolor sit amet, consectetur adipiscing</p>
  <div class="field" style="top:68px">Name:</div>
  <div class="field" style="top:91px">School:</div>
  <div class="field" style="top:114px">Email:</div>
  <div class="field" style="top:137px">Please Select:
    <span class="select-caret"><svg width="6" height="4" viewBox="0 0 6 4"><path d="M0 0h6L3 4z" fill="#555"/></svg></span>
  </div>
  <div class="comments">Comments:</div>
  <div class="submit">SUBMIT</div>
</section>

<footer class="abs footer">
  <div class="brand"><span class="brand-mark"></span>TovaRoom</div>
  <p class="about-text">Lorem ipsum dolor sit amet, consectetur adi ising elit,sed do eiusmod tempor incididunt ut labore et dolore magndolore magna.</p>

  <h3 style="left:258px">Links</h3>
  <ul class="footer-links">
    <li>Home</li><li>About us</li><li>How it works</li><li>Services</li><li>Why use us</li><li>FAQ</li>
  </ul>

  <h3 style="left:356px">Contact</h3>
  <ul class="contact">
    <li><svg width="5" height="7" viewBox="0 0 5 7"><path d="M2.5 0A2.5 2.5 0 0 0 0 2.5C0 4.5 2.5 7 2.5 7S5 4.5 5 2.5A2.5 2.5 0 0 0 2.5 0z" fill="#ddd"/></svg><span>Address: Lorem ipsolorsit,<br>dummy location 584, Location<br>Dummy lorem ipsum.</span></li>
    <li><svg width="6" height="6" viewBox="0 0 6 6"><path d="M1 0l1.3 1.5-.7 1a4 4 0 0 0 1.9 1.9l1-.7L6 5l-1 1C2 6 0 4 0 1z" fill="#ddd"/></svg><span>Phone: 555-310-7742</span></li>
    <li><svg width="6" height="5" viewBox="0 0 6 5"><rect width="6" height="5" fill="#ddd"/><path d="M0 0l3 2.5L6 0" stroke="#3d3d3f" fill="none" stroke-width=".7"/></svg><span>Email:info@tovaroom-mail.net</span></li>
  </ul>

  <h3 style="left:521px">Follow Us</h3>
  <div class="social" aria-label="Social links"><span></span><span></span><span></span><span></span></div>

  <div class="divider"></div>
  <p class="copyright">©2017 Tovaroom All Rights Reserved | Legal and Privacy Statement. Site Map</p>
</footer>

</body>
</html>
```